Oven Cleaning flyer design

Hi there,
I need help designing a letterbox flyer. It needs to be DL size.
I have attached a rough design made with Chat GPT.
Would like back and front, have my business colors.
Please find attached mock up of what I would roughly like.
Also find attached logo.
Thank you

Target Market(s)

Home owners over 40

Industry/Entity Type

Cleaning

Requirements
Must have
• Logo, before after of oven, brand colors

```html
<!DOCTYPE html>
<html lang="en">
<head>
<meta charset="utf-8">
<title>Bright Bake Cleaning – DL Flyer</title>
<link rel="stylesheet" href="https://fonts.googleapis.com/css2?family=Montserrat:wght@400;500;600;700;800;900&display=swap">
<style>
  :root{
    --bg:#4a4840;
    --navy:#1f2a55;
    --teal:#3fbfc6;
    --ink:#111318;
    --white:#ffffff;
    --rule:#c9cdd3;
    --gold:#d9a935;
    --gold-dark:#a97a17;
    --star:#1c9ad6;
  }
  *{box-sizing:border-box;margin:0;padding:0}
  html,body{width:1200px;height:2333px;overflow:hidden;background:var(--bg)}
  body{position:relative;font-family:"Montserrat",sans-serif;color:var(--ink)}
  .flyer{position:absolute;top:612px;width:540px;height:1108px;background:var(--white);overflow:hidden;box-shadow:0 6px 18px rgba(0,0,0,.35)}
  .flyer--front{left:40px}
  .flyer--back{left:620px}
  .abs{position:absolute}
  .band{position:absolute;left:0;top:0;width:540px;height:1108px}

  /* brand */
  .brand{left:0;right:0;top:52px;display:flex;align-items:center;justify-content:center;gap:20px}
  .brand__dot{width:84px;height:84px;border-radius:50%;background:var(--teal)}
  .brand__name{font-weight:800;font-size:38px;line-height:1.02;color:var(--teal);text-transform:uppercase;letter-spacing:1px}

  .headline{left:0;right:0;top:212px;text-align:center}
  .headline__lead{font-weight:500;font-size:56px;line-height:1;color:var(--ink);letter-spacing:-.5px}
  .headline__accent{font-weight:800;font-size:58px;line-height:1;color:var(--teal);margin-top:2px}
  .intro{left:60px;right:60px;top:342px;text-align:center;font-weight:600;font-size:19px;line-height:25px}

  .divider{width:2px;background:var(--rule)}
  .front-divider{left:269px;top:470px;height:510px}

  .compare__label{top:482px;font-weight:800;font-size:22px;color:var(--navy);text-align:center;width:222px}
  .compare__label--before{left:34px}
  .compare__label--after{left:284px}
  .compare__photo{top:510px;width:222px;height:312px;border:5px solid var(--teal);border-radius:22px}
  .compare__photo--before{left:34px;background:linear-gradient(170deg,#4a4743 0%,#6b5a46 45%,#a4703a 70%,#8f5a2a 100%)}
  .compare__photo--after{left:284px;background:linear-gradient(170deg,#e9eaec 0%,#8d9096 40%,#3a3c40 70%,#b9bcc1 100%)}

  .seal{border-radius:50%;background:radial-gradient(circle at 40% 35%,#f6d36b 0%,var(--gold) 55%,var(--gold-dark) 100%)}
  .seal--front{left:370px;top:818px;width:130px;height:130px}
  .seal--back{left:305px;top:745px;width:200px;height:200px}

  .cta{left:34px;right:20px;top:934px;color:var(--white)}
  .cta__lead{font-weight:400;font-size:27px;line-height:1.1}
  .cta__main{font-weight:700;font-size:31px;line-height:1.15}
  .cta__phone{display:flex;align-items:center;gap:12px;margin-top:12px;font-weight:800;font-size:50px;line-height:1;color:var(--teal)}
  .cta__web{display:flex;align-items:center;gap:14px;margin-top:4px;font-weight:700;font-size:21px;color:var(--teal)}
  .icon{flex:none}

  /* back */
  .why{left:0;right:0;top:28px;text-align:center}
  .why__lead{font-weight:800;font-size:34px;line-height:1.05;color:var(--navy);letter-spacing:-.5px}
  .why__name{font-weight:500;font-size:32px;line-height:1.1;color:var(--teal)}
  .about{left:36px;right:36px;top:122px;text-align:center;font-weight:500;font-size:17.5px;line-height:25.5px}

  .offer{left:0;right:0;top:300px;text-align:center}
  .offer__amount{font-size:98px;line-height:1;color:var(--navy);letter-spacing:-2px}
  .offer__amount b{font-weight:900}
  .offer__amount span{font-weight:600}
  .offer__sub{font-weight:600;font-size:40px;line-height:1;color:var(--teal);margin-top:-4px}

  .back-divider{left:268px;top:462px;height:515px}
  .perks{left:42px;top:532px;list-style:none}
  .perks li{display:flex;align-items:center;gap:12px;font-weight:700;font-size:23px;line-height:25px;color:var(--ink);margin-bottom:16px}
  .extras{left:294px;top:538px;font-size:31px;line-height:34px}
  .extras__lead{font-weight:600;color:var(--teal)}
  .extras__list{font-weight:800;color:var(--ink)}
  .extras__list span{color:var(--teal)}
</style>
</head>
<body>

<!-- FRONT -->
<section class="flyer flyer--front">
  <div class="abs brand">
    <div class="brand__dot"></div>
    <div class="brand__name">Bright Bake<br>Cleaning</div>
  </div>

  <div class="abs headline">
    <div class="headline__lead">Bring Your Oven</div>
    <div class="headline__accent">Back to Life</div>
  </div>
  <p class="abs intro">Professional, non-caustic oven cleaning that removes built-up grease, smoke, and burnt grime-leaving your oven looking fresh again.</p>

  <div class="abs divider front-divider"></div>
  <div class="abs compare__label compare__label--before">BEFORE</div>
  <div class="abs compare__label compare__label--after">AFTER</div>
  <div class="abs compare__photo compare__photo--before" role="img" aria-label="Photo of a greasy, burnt oven interior before cleaning"></div>
  <div class="abs compare__photo compare__photo--after" role="img" aria-label="Photo of the same oven interior clean after service"></div>

  <svg class="band" viewBox="0 0 540 1108" aria-hidden="true">
    <path d="M0 805 Q250 935 540 905 L540 1108 L0 1108 Z" fill="var(--navy)"/>
    <path d="M0 805 Q70 850 140 875 Q340 945 540 850 L540 905 Q250 935 0 805 Z" fill="var(--teal)"/>
  </svg>
  <div class="abs seal seal--front"></div>

  <div class="abs cta">
    <div class="cta__lead">Call Now for</div>
    <div class="cta__main">Fast, Professional Service</div>
    <div class="cta__phone">
      <svg class="icon" width="26" height="26" viewBox="0 0 24 24"><circle cx="12" cy="12" r="12" fill="#fff"/><path d="M8.6 6.5l1.6 2.4-1 1.2c.7 1.6 2 2.9 3.6 3.6l1.2-1 2.4 1.6-.8 2c-4.4.3-9.3-4.6-9-9z" fill="var(--navy)"/></svg>
      <span>0412 555 018</span>
    </div>
    <div class="cta__web">
      <svg class="icon" width="24" height="24" viewBox="0 0 24 24" fill="none" stroke="#fff" stroke-width="1.8"><circle cx="12" cy="12" r="10"/><ellipse cx="12" cy="12" rx="4.5" ry="10"/><path d="M2 12h20M4 7h16M4 17h16"/></svg>
      <span>www.brightbakecleaning.com.au</span>
    </div>
  </div>
</section>

<!-- BACK -->
<section class="flyer flyer--back">
  <div class="abs why">
    <div class="why__lead">WHY CHOOSE</div>
    <div class="why__name">BRIGHT BAKE CLEANING?</div>
  </div>
  <p class="abs about">we're a local family business providing professional, non-caustic oven cleaning across Sunshine Coast. Using specialized-equipment and proven cleaning methods, we remove heavy grease, carbon build-up. smoke residue, restoring your oven safely and effectively.</p>

  <div class="abs offer">
    <div class="offer__amount"><b>$10</b> <span>OFF</span></div>
    <div class="offer__sub">your first clean</div>
  </div>

  <div class="abs divider back-divider"></div>
  <ul class="abs perks">
    <li><svg class="icon" width="28" height="28" viewBox="0 0 24 24"><path d="M12 0 L14 10 L24 12 L14 14 L12 24 L10 14 L0 12 L10 10 Z" fill="var(--star)"/></svg><span>Reliable<br>Service</span></li>
    <li><svg class="icon" width="28" height="28" viewBox="0 0 24 24"><path d="M12 0 L14 10 L24 12 L14 14 L12 24 L10 14 L0 12 L10 10 Z" fill="var(--star)"/></svg><span>Non-Caustic<br>Cleaning</span></li>
    <li><svg class="icon" width="28" height="28" viewBox="0 0 24 24"><path d="M12 0 L14 10 L24 12 L14 14 L12 24 L10 14 L0 12 L10 10 Z" fill="var(--star)"/></svg><span>Satisfaction<br>Guaranteed</span></li>
  </ul>
  <div class="abs extras">
    <div class="extras__lead">We also<br>clean</div>
    <div class="extras__list">cooktops<span>,</span><br>rangehoods<br><span>&amp;</span> BBQs</div>
  </div>

  <svg class="band" viewBox="0 0 540 1108" aria-hidden="true">
    <path d="M0 805 Q250 935 540 905 L540 1108 L0 1108 Z" fill="var(--navy)"/>
    <path d="M0 805 Q70 850 140 875 Q340 945 540 850 L540 905 Q250 935 0 805 Z" fill="var(--teal)"/>
  </svg>
  <div class="abs seal seal--back"></div>

  <div class="abs cta">
    <div class="cta__lead">Call Now for</div>
    <div class="cta__main">Fast, Professional Service</div>
    <div class="cta__phone">
      <svg class="icon" width="26" height="26" viewBox="0 0 24 24"><circle cx="12" cy="12" r="12" fill="#fff"/><path d="M8.6 6.5l1.6 2.4-1 1.2c.7 1.6 2 2.9 3.6 3.6l1.2-1 2.4 1.6-.8 2c-4.4.3-9.3-4.6-9-9z" fill="var(--navy)"/></svg>
      <span>0412 555 018</span>
    </div>
    <div class="cta__web">
      <svg class="icon" width="24" height="24" viewBox="0 0 24 24" fill="none" stroke="#fff" stroke-width="1.8"><circle cx="12" cy="12" r="10"/><ellipse cx="12" cy="12" rx="4.5" ry="10"/><path d="M2 12h20M4 7h16M4 17h16"/></svg>
      <span>www.brightbakecleaning.com.au</span>
    </div>
  </div>
</section>

</body>
</html>
```